Youth Sports Banner Ad - 3x5 ft banner special!

We are looking for a full page ad (8.5x11") to advertise our banner services for Youth Sports leagues. The flyers will be handed out to teams and parents in hopes to draw their business to us for team banners.
We want to show our logo, address (4187 Verbena Ln. Paso Robles). Please include that we are offering a youth sports special price on 3x5 ft team banners for $115 (plus tax). The pricing will include 1 layout with up to 2 revisions. We would like the ad to grab the attention of the audience and ask them to "Call, Email or Stop in Today!"

Our info that needs to be on the banner includes:
email: info@markwell47.net
phone: 805-291-6583

We want to really focus on our quick turnaround as we will be producing the banners withing 1-2 business days after artwork approval.
We would like to include the banner samples if possible, and if you see fit, also include that we would like the potential customer to email us their teams name, roster, and colors to help speed up the layout process.

Target Market(s)

Parents of kids playing youth sports. The flyer is meant to increase awareness of our sign shop, while offering a great discount on banners for youth sports banners.

Font styles to use
Sans Serif

Colors

Designer to choose colors to be used in the design.

Requirements
Must have
• Our logo, $115 plus tax banner price, our business information, request to send over all team information including name, roster, and team colors.
Nice to have
• Would like to see color in the ad! If you can tie in the Kelly green from our logo, that would be great.

```html
<!DOCTYPE html>
<html lang="en">
<head>
<meta charset="utf-8">
<title>3x5 ft Team Banner Special – Markwell Signs</title>
<link rel="stylesheet" href="https://fonts.googleapis.com/css2?family=Montserrat:wght@600;700;800;900&family=Open+Sans:ital,wght@1,600;1,700;1,800&family=Oswald:wght@600&family=Lobster&family=Righteous&display=swap">
<style>
  :root{
    --sky-top:#1778cf;
    --sky-mid:#2ba4ea;
    --sky-low:#eaf7fd;
    --kelly:#1fa23a;
    --ink:#1c1c1f;
    --navy:#1d2a55;
    --white:#ffffff;
    --rocket-purple:#3a2f8a;
    --rocket-dark:#1b1744;
    --comet-orange:#f07f1e;
  }
  *{margin:0;padding:0;box-sizing:border-box}
  html,body{width:934px;height:1200px;overflow:hidden}
  body{position:relative;background:linear-gradient(180deg,var(--sky-top) 0%,var(--sky-mid) 48%,#8fd2f4 78%,var(--sky-low) 100%);font-family:"Montserrat",sans-serif;color:var(--ink)}
  .abs{position:absolute}

  .hero-photo{left:0;top:0;width:934px;height:330px;background:linear-gradient(180deg,#1a3f9a 0%,#2456b5 55%,rgba(34,110,200,0) 100%)}

  .headline-size{left:180px;top:254px;font:800 82px/1 "Montserrat",sans-serif;color:var(--white);text-shadow:3px 4px 0 rgba(0,0,0,.35)}
  .headline-team{left:486px;top:214px;font:400 122px/1 "Lobster",cursive;color:var(--white);text-shadow:3px 4px 0 rgba(0,0,0,.35)}

  .special-band{left:36px;top:324px;width:868px;height:166px}
  .special-title{left:0;top:350px;width:934px;text-align:center;font:900 80px/1 "Montserrat",sans-serif;letter-spacing:-1px;color:var(--ink)}
  .special-lede{left:0;top:420px;width:934px;text-align:center;font:italic 700 22px/1.42 "Open Sans",sans-serif;color:var(--white)}
  .special-lede b{font-size:28px;font-weight:800}

  .promise-bar{left:56px;top:492px;width:796px;height:64px}
  .promise-family{left:84px;top:513px;font:700 20px/1 "Montserrat",sans-serif;color:var(--white)}
  .promise-icon{left:486px;top:500px}
  .promise-quick{left:546px;top:514px;font:400 21px/1 "Righteous",sans-serif;color:var(--ink);letter-spacing:4px}

  .fine-print{left:0;top:571px;width:934px;text-align:center;font:italic 600 13.5px/1 "Open Sans",sans-serif;color:var(--white)}

  .sample{box-shadow:4px 6px 10px rgba(0,0,0,.35)}
  .sample-rockets{left:50px;top:630px;width:396px;height:226px;background:var(--rocket-purple);transform:rotate(-4deg);color:var(--white);font:700 15px/1 "Montserrat",sans-serif}
  .sample-rockets .roster{position:absolute;display:flex;flex-direction:column;gap:12px}
  .sample-rockets .roster-left{left:14px;top:28px}
  .sample-rockets .roster-right{right:14px;top:24px;text-align:right}
  .sample-rockets .mascot{position:absolute;left:128px;top:36px;width:140px;height:124px;border-radius:50%;background:radial-gradient(#2a2a60,var(--rocket-dark))}
  .sample-rockets .footer{position:absolute;left:0;bottom:0;width:100%;height:28px;background:var(--rocket-dark);display:flex;justify-content:space-between;align-items:center;padding:0 14px;font-size:12px}

  .ask-heading{left:470px;top:618px;width:405px;text-align:center;font:italic 700 23px/1.15 "Open Sans",sans-serif;color:var(--navy)}

  .sample-comets{left:458px;top:706px;width:430px;height:258px;background:#0d0d0d;transform:rotate(4deg);color:var(--white);font:600 19px/1 "Oswald",sans-serif;letter-spacing:1.5px}
  .sample-comets .mascot{position:absolute;left:18px;top:14px;width:110px;height:174px;border-radius:40px;background:linear-gradient(180deg,var(--comet-orange),#b55a10)}
  .sample-comets .team-name{position:absolute;left:160px;top:16px;width:250px;text-align:center;font:600 44px/0.95 "Oswald",sans-serif;color:var(--comet-orange);letter-spacing:3px}
  .sample-comets .player{position:absolute}
  .sample-comets .coaches{position:absolute;left:30px;top:204px;font-size:12px;letter-spacing:1px}
  .sample-comets .footer{position:absolute;left:0;bottom:0;width:100%;height:24px;background:var(--comet-orange);color:var(--ink);font-size:11px;display:flex;align-items:center;padding-left:10px;gap:10px}

  .cta{left:100px;top:878px;transform:rotate(-4deg);font:italic 700 25px/1 "Open Sans",sans-serif;color:var(--navy)}

  .brand{left:84px;top:960px;width:220px}
  .brand-mark{width:18px;height:18px;background:var(--kelly);margin-bottom:10px}
  .brand-name{font:800 36px/1 "Montserrat",sans-serif;color:var(--kelly);letter-spacing:-0.5px}

  .contact-line{left:300px;width:620px;text-align:center}
  .contact-address{top:1000px;font:700 19px/1 "Montserrat",sans-serif;color:var(--ink)}
  .contact-email{top:1028px;font:400 44px/1 "Righteous",sans-serif;color:var(--ink);letter-spacing:5px}
  .contact-phone{top:1074px;font:400 50px/1 "Righteous",sans-serif;color:var(--ink);letter-spacing:3px}
  .contact-services{top:1134px;font:italic 600 15px/1.4 "Open Sans",sans-serif;color:var(--kelly)}
</style>
</head>
<body>
  <div class="abs hero-photo" role="img" aria-label="Photo of a youth soccer team in blue jerseys huddled together"></div>

  <div class="abs headline-size">3x5 ft.</div>
  <div class="abs headline-team">Team</div>

  <svg class="abs special-band" viewBox="0 0 868 166" aria-hidden="true">
    <defs><linearGradient id="bandGreen" x1="0" y1="0" x2="0" y2="1"><stop offset="0" stop-color="#6cc13f"/><stop offset="1" stop-color="#1f9a3c"/></linearGradient></defs>
    <path d="M70 0 H856 Q868 0 864 12 L826 153 Q822 166 808 166 H12 Q0 166 4 153 L50 12 Q54 0 70 0Z" fill="url(#bandGreen)"/>
  </svg>
  <div class="abs special-title">BANNER SPECIAL</div>
  <div class="abs special-lede">As a longtime supporter and sponsor of local sports, we are offering<br>discounted pricing for <b>3x5 ft</b> banners for local youth sports!</div>

  <svg class="abs promise-bar" viewBox="0 0 796 64" aria-hidden="true">
    <path d="M14 0 H560 L540 64 H8 Q0 64 2 56 L8 8 Q10 0 14 0Z" fill="#1c1c1f"/>
    <path d="M440 0 H790 Q796 0 794 8 L784 56 Q782 64 774 64 H420 L440 0Z" fill="#fff"/>
  </svg>
  <div class="abs promise-family">FAMILY OWNED AND OPERATED</div>
  <svg class="abs promise-icon" width="48" height="48" viewBox="0 0 48 48" aria-hidden="true">
    <path d="M24 5 A19 19 0 1 0 43 24" fill="none" stroke="#1c1c1f" stroke-width="4"/>
    <path d="M38 8 L44 18 L32 18Z" fill="#1c1c1f"/>
    <circle cx="24" cy="24" r="11" fill="none" stroke="#1c1c1f" stroke-width="3"/>
    <path d="M24 17 V24 H29" fill="none" stroke="#1c1c1f" stroke-width="3"/>
  </svg>
  <div class="abs promise-quick">QUICK TURNAROUND</div>

  <div class="abs fine-print">Youth Sports Special price on 3x5 ft team banners for $115 (plus tax).&nbsp; Price includes 1 layout with up to 2 revisions.</div>

  <div class="abs sample sample-rockets">
    <div class="roster roster-left"><span>#9 ELLIOT</span><span>#5 ROWAN</span><span>#4 MILES</span><span>#6 GAVIN</span><span>#2 DEREK</span><span>#7 MATEO</span></div>
    <div class="mascot" role="img" aria-label="Red Rockets team mascot and lettered team name"></div>
    <div class="roster roster-right"><span>#11 BECKETT</span><span>#10 NOLAN</span><span>#3 SILAS</span><span>#12 JONAH</span><span>#8 WESLEY</span><span>#13 AUGUST</span></div>
    <div class="footer"><span>HEAD COACH DELGADO</span><span>SPONSORED BY HALLOWAY'S</span></div>
  </div>

  <div class="abs ask-heading">Just Email Us Your Team's Name ,<br>Roster, and Colors and<br>We'll Do The Rest!</div>

  <div class="abs sample sample-comets">
    <div class="mascot" role="img" aria-label="Orange team mascot holding a baseball"></div>
    <div class="team-name">VALLEY<br>COMETS</div>
    <span class="player" style="left:150px;top:118px">QUINN</span>
    <span class="player" style="left:234px;top:118px">ABEL</span>
    <span class="player" style="left:302px;top:118px">REID</span>
    <span class="player" style="left:358px;top:118px">ROMAN</span>
    <span class="player" style="left:150px;top:158px">HAYES</span>
    <span class="player" style="left:246px;top:158px">BRANSON</span>
    <span class="player" style="left:346px;top:158px">MARLEY</span>
    <div class="coaches">COACHES: DANA WHITFIELD&nbsp; CARLA JENNINGS</div>
    <div class="footer"><span>SPONSOR: OAK GROVE SENIOR CARE</span><span>•</span><span>TEAM MOM: TESSA MARLOWE</span></div>
  </div>

  <div class="abs cta">Call, Email or Stop in Today!</div>

  <div class="abs brand">
    <div class="brand-mark"></div>
    <div class="brand-name">MARKWELL<br>SIGNS</div>
  </div>

  <div class="abs contact-line contact-address">4187 VERBENA LN. PASO ROBLES</div>
  <div class="abs contact-line contact-email">info@markwell47.net</div>
  <div class="abs contact-line contact-phone">(805) 291 - 6583</div>
  <div class="abs contact-line contact-services">(Other services include: vehicle graphics, storefront signs, safety signs and<br>reflective signs and more!)</div>
</body>
</html>
```